Halloway Consulting Cover 2 - Smart Capital

Halloway Consulting is a business consulting firm. We will publish a series of four thought leadership pieces online and via PDF. The second of the series is attached to this project. We need an eye-catching cover page with a back page that keeps with our branding. The document attached is in the final draft, and the cover and pack pages are placeholders only. You can find more about our branding and style on our website www.hallowayconsulting.com.au. The other three projects can be found here with a similar brief, and you are welcome to submit a design for all 4.

```html
<!DOCTYPE html>
<html lang="en">
<head>
<meta charset="utf-8">
<title>Halloway Consulting – Smart Capital Cover and Back Page</title>
<link rel="stylesheet" href="https://fonts.googleapis.com/css2?family=Raleway:wght@400;500;800;900&family=Hind:wght@400;600&display=swap">
<style>
  :root {
    --orange: #f7931e;
    --blue: #00aeef;
    --ink: #1b1b1b;
    --white: #ffffff;
    --stage: #000000;
    --sky: #c9dbf6;
    --concrete: #8d8f8f;
  }
  * { box-sizing: border-box; margin: 0; padding: 0; }
  html, body { width: 1200px; height: 804px; overflow: hidden; background: var(--stage); }
  .spread { position: relative; width: 1200px; height: 804px; }
  .page {
    position: absolute; top: 38px; width: 516px; height: 729px;
    background: var(--white); overflow: hidden;
    font-family: "Raleway", sans-serif;
  }
  .page--cover { left: 65px; }
  .page--back { left: 620px; }

  /* Cover */
  .cover-art { position: absolute; left: 0; top: 0; }
  .cover-title { position: absolute; left: 0; width: 100%; text-align: center; z-index: 1; }
  .cover-title__main {
    top: 19px; font-size: 50px; font-weight: 900; color: var(--orange);
    letter-spacing: 0.5px; line-height: 1;
  }
  .cover-title__sub {
    top: 63px; font-size: 30px; font-weight: 900; color: var(--blue);
    line-height: 30px; letter-spacing: 0.2px;
  }
  .cover-tagline {
    position: absolute; top: 149px; left: 0; width: 100%; text-align: center;
    font-size: 17px; font-weight: 500; color: var(--ink); z-index: 1;
  }

  .brand {
    position: absolute; display: flex; align-items: center; gap: 12px;
  }
  .brand__dot { width: 46px; height: 46px; border-radius: 50%; background: var(--blue); flex: none; }
  .brand__name {
    font-family: "Raleway", sans-serif; font-weight: 800; color: var(--ink);
    font-size: 25px; line-height: 26px;
  }
  .brand--cover { left: 150px; top: 600px; }
  .brand--back { left: 150px; top: 40px; }

  .footer-band {
    position: absolute; left: 0; bottom: 0; width: 100%; height: 44px;
    display: flex; align-items: center; color: var(--white);
  }
  .footer-band--orange { background: var(--orange); justify-content: center; }
  .footer-band--blue { background: var(--blue); padding: 0 22px; }
  .web-link { display: flex; align-items: center; gap: 7px; font-size: 17px; font-weight: 500; }
  .web-link svg { width: 12px; height: 12px; }

  /* Back */
  .back-photo {
    position: absolute; left: 15px; top: 150px; width: 488px; height: 298px;
    border-radius: 24px;
    background: linear-gradient(160deg, var(--sky) 0%, #b9c8dc 28%, #9a9c9c 52%, var(--concrete) 100%);
  }
  .cta-band {
    position: absolute; left: 0; top: 490px; width: 100%; height: 50px;
    background: linear-gradient(90deg, var(--blue) 0%, var(--blue) 22%, #4fa7a0 55%, var(--orange) 92%);
    color: var(--white); text-align: center; font-size: 16.5px; line-height: 20px;
    padding-top: 5px;
  }
  .contact { position: absolute; font-family: "Hind", sans-serif; color: var(--ink); }
  .contact--first { left: 22px; top: 578px; }
  .contact--second { left: 283px; top: 576px; }
  .contact__name { font-weight: 600; font-size: 17px; line-height: 20px; }
  .contact__role { font-size: 13px; line-height: 16px; margin-bottom: 8px; }
  .contact__line { font-size: 12.5px; line-height: 16px; }
  .contact__line b { font-weight: 600; }
  .contact__line u { text-underline-offset: 2px; }

  .follow { margin-left: auto; display: flex; align-items: center; gap: 12px; }
  .follow__label { font-size: 11px; font-weight: 800; margin-right: 4px; }
  .follow__icon { width: 13px; height: 13px; background: var(--white); border-radius: 2px; }
</style>
</head>
<body>
<main class="spread">

  <section class="page page--cover">
    <svg class="cover-art" width="516" height="729" viewBox="0 0 516 729">
      <defs>
        <linearGradient id="chevronFill" x1="0" y1="320" x2="0" y2="390" gradientUnits="userSpaceOnUse">
          <stop offset="0" stop-color="#00aeef"/>
          <stop offset="1" stop-color="#f7931e"/>
        </linearGradient>
        <linearGradient id="photoTone" x1="0.2" y1="0" x2="0.8" y2="1">
          <stop offset="0" stop-color="#d6e6fb"/>
          <stop offset="0.3" stop-color="#b3c4dc"/>
          <stop offset="0.5" stop-color="#9c9e9e"/>
          <stop offset="1" stop-color="#6f7171"/>
        </linearGradient>
      </defs>
      <path class="chevron-band" fill="url(#chevronFill)"
            d="M0 280 L74 316 L74 438 Q74 449 84 454 L250 550 Q258 554 266 550 L431 454 Q441 449 441 438 L441 316 L516 280 L516 474 L272 582 Q258 588 244 582 L0 475 Z"/>
      <polygon role="img" aria-label="Upward view of a concrete tower against a pale sky"
               points="258,203 417,280 417,440 258,529 96,440 96,280"
               fill="url(#photoTone)" stroke="url(#photoTone)" stroke-width="16" stroke-linejoin="round"/>
    </svg>

    <h1 class="cover-title cover-title__main">SMART CAPITAL :</h1>
    <h2 class="cover-title cover-title__sub">PARTNERING WITH FUNDS<br>TO SCALE YOUR BUSINESS</h2>
    <p class="cover-tagline">Bridging Valuation Gaps in Fund Raising</p>

    <div class="brand brand--cover">
      <span class="brand__dot"></span>
      <span class="brand__name">Halloway<br>Consulting</span>
    </div>

    <footer class="footer-band footer-band--orange">
      <span class="web-link">
        <svg viewBox="0 0 12 12" fill="none" stroke="currentColor" stroke-width="1.1"><circle cx="6" cy="6" r="5"/><ellipse cx="6" cy="6" rx="2.2" ry="5"/><line x1="1" y1="6" x2="11" y2="6"/></svg>
        hallowayconsulting.com.au
      </span>
    </footer>
  </section>

  <section class="page page--back">
    <div class="brand brand--back">
      <span class="brand__dot"></span>
      <span class="brand__name">Halloway<br>Consulting</span>
    </div>

    <div class="back-photo" role="img" aria-label="Upward view of a concrete tower against a pale sky"></div>

    <p class="cta-band">Contact us to find out how Halloway Consulting can<br>help build your compny into a market leader today.</p>

    <div class="contact contact--first">
      <p class="contact__name">Daniel Halloway</p>
      <p class="contact__role">Managing Director</p>
      <p class="contact__line"><b>Mobile</b> +61 400 318 206</p>
      <p class="contact__line"><b>Email</b> <u>daniel@hallowayconsulting.com.au</u></p>
    </div>
    <div class="contact contact--second">
      <p class="contact__name">Marcus Halloway</p>
      <p class="contact__role">Managing Director</p>
      <p class="contact__line"><b>Mobile</b> +61 400 529 781</p>
      <p class="contact__line"><b>Email</b> <u>marcus@hallowayconsulting.com.au</u></p>
    </div>

    <footer class="footer-band footer-band--blue">
      <span class="web-link">
        <svg viewBox="0 0 12 12" fill="none" stroke="currentColor" stroke-width="1.1"><circle cx="6" cy="6" r="5"/><ellipse cx="6" cy="6" rx="2.2" ry="5"/><line x1="1" y1="6" x2="11" y2="6"/></svg>
        hallowayconsulting.com.au
      </span>
      <span class="follow">
        <span class="follow__label">Follow us</span>
        <span class="follow__icon"></span>
        <span class="follow__icon"></span>
      </span>
    </footer>
  </section>

</main>
</body>
</html>
```